Book cover for a New Adult, romance/ contemporary novel.

I need a full front, back, and spine cover for my upcoming book. The novel is a romance/ coming of age book and is similar to Every Quiet Harbor by Marissa Colfax. My main audience is women in their late teens/ early 20's. The book is an emotional, reminiscent piece and I would love to see some cover designs with a darker palette like Waiting on Belmora, Nine Rooms Between, or Bartholomew and Kip (but I also adore some lighter covers, especially those that feature the couple such as A Different Then or Past Each Hour). Feel free to send some minimal designs as well if you have any! A great idea of that would be the cover for Salt and Clover or Waiting on Belmora. If you go with a minimal design, I'd love to see silhouettes or maybe a burning candle. Another possible idea I thought of would be a scene at a concert with the crowd silhouetted and then my main character (more details on her below) standing in the middle of it all. I prefer animation/drawing etc over real models. But feel free to send me whatever you think might match the vibe, I'd love to see anything you have in mind! Some main symbols in my book are stars and candles. The main character (Marisol) is a female Korean with brown, medium length straight hair, and the love interest (Theo) is a tall and thin male Caucasian with curly brown hair. The book is openly emotional, wistful, and sets an ache in your chest, so I can't wait to see what designs you artists come up with! (My barcode will need to be included on the back cover, and I am getting that soon!)
The title is "The Weight of Daylight" and the author's name is Brenna Quill. The book's dimensions will be 5.5x8.25. The blurb for the back cover is:
When happily ever falls apart, all you can do is move forward… and reminisce. Marisol Ahn returns home from college following a tragic incident she can’t bring herself to talk about and a breakup with her boyfriend, Theo Marsh. Finding it difficult to confront her traumas, she begins therapy. Marisol takes the therapist on a rollercoaster journey of her college life, retelling the events that caused her relationship to spiral out of control and led to her dropping out of pre-med despite that being her life-long dream. Marisol sets out to remember how things were before everything got so messed up, and figure out how to continue living now that they are.
The author bio for the back cover is:
Brenna Quill is the author of The Restless and Bold. She is a self published writer from Las Vegas who likes to pretend she’s currently in a New York bookstore, drinking a latte, while listening to a carefully curated playlist. When she’s not writing, Brenna is taking care of her plant babies and cuddling with the cutest puppy in the world.

```html
<!DOCTYPE html>
<html lang="en">
<head>
<meta charset="utf-8">
<title>The Weight of Daylight — Full Cover</title>
<link rel="stylesheet" href="https://fonts.googleapis.com/css2?family=Kaushan+Script&family=Homemade+Apple&family=Noto+Serif:ital,wght@0,400;0,700;1,400&family=Poppins:wght@400&display=swap">
<style>
  :root {
    --navy: #1b1f3f;
    --navy-deep: #181c38;
    --peach: #e8bf96;
    --white: #ffffff;
    --scene-blue: #2c4a85;
    --scene-shadow: #202a52;
    --scene-warm: #7a3a2a;
  }
  * { margin: 0; padding: 0; box-sizing: border-box; }
  html, body { width: 1200px; height: 842px; overflow: hidden; background: var(--navy); }
  .cover {
    position: relative;
    width: 1200px; height: 842px;
    background: var(--navy);
    overflow: hidden;
    color: var(--white);
  }
  .star-field { position: absolute; inset: 0; width: 1200px; height: 842px; }
  .star-field circle { fill: var(--white); }

  /* Back cover */
  .tagline {
    position: absolute; left: 60px; width: 476px; top: 160px;
    text-align: center;
    font-family: "Homemade Apple", cursive;
    font-size: 19px; line-height: 28px; letter-spacing: 0.16em;
    color: var(--peach);
  }
  .blurb {
    position: absolute; left: 66px; width: 464px; top: 268px;
    text-align: center;
    font-family: "Noto Serif", serif;
    font-size: 17.5px; line-height: 24px; letter-spacing: 0.02em;
    color: var(--white);
  }
  .author-bio {
    position: absolute; left: 44px; width: 308px; top: 697px;
    font-family: "Noto Serif", serif;
    font-size: 11.2px; line-height: 14.4px;
    color: var(--white);
  }
  .barcode-area {
    position: absolute; left: 376px; top: 711px;
    width: 140px; height: 76px;
    border: 1.5px solid var(--white);
  }

  /* Spine */
  .spine-author {
    position: absolute; left: 601px; top: 252px;
    transform: translate(-50%, -50%) rotate(-90deg);
    white-space: nowrap;
    font-family: "Poppins", sans-serif;
    font-size: 22px; letter-spacing: 0.22em;
    color: var(--white);
  }
  .spine-title {
    position: absolute; left: 602px; top: 584px;
    transform: translate(-50%, -50%) rotate(-90deg);
    white-space: nowrap;
    font-family: "Kaushan Script", cursive;
    font-size: 33px;
    color: var(--peach);
  }

  /* Front cover */
  .front-title {
    position: absolute; left: 740px; width: 360px; top: 62px;
    text-align: center;
    font-family: "Kaushan Script", cursive;
    color: var(--peach);
    line-height: 1;
  }
  .front-title span { display: block; }
  .front-title .word-small { font-size: 50px; }
  .front-title .word-large { font-size: 82px; margin: 2px 0; }
  .front-title .word-of { font-size: 44px; }
  .front-author {
    position: absolute; left: 770px; width: 300px; top: 388px;
    text-align: center;
    font-family: "Poppins", sans-serif;
    font-size: 26px; letter-spacing: 0.2em;
    color: var(--white);
  }
  .cover-illustration {
    position: absolute; left: 639px; top: 440px; width: 561px; height: 402px;
    background:
      radial-gradient(ellipse 35% 55% at 55% 85%, rgba(192,58,36,0.55), transparent 70%),
      radial-gradient(ellipse 30% 45% at 55% 45%, rgba(122,58,42,0.5), transparent 75%),
      linear-gradient(90deg, var(--scene-blue) 0%, var(--scene-shadow) 60%, var(--navy-deep) 100%);
    -webkit-mask-image: linear-gradient(180deg, transparent 0%, #000 18%);
            mask-image: linear-gradient(180deg, transparent 0%, #000 18%);
  }
</style>
</head>
<body>
<main class="cover">
  <svg class="star-field" viewBox="0 0 2296 1612" preserveAspectRatio="none" aria-hidden="true">
    <circle cx="136" cy="93" r="4.5"/><circle cx="391" cy="92" r="4.5"/><circle cx="584" cy="62" r="4.5"/>
    <circle cx="969" cy="79" r="4.5"/><circle cx="442" cy="157" r="4.5"/><circle cx="74" cy="212" r="4.5"/>
    <circle cx="709" cy="198" r="4.5"/><circle cx="267" cy="255" r="4.5"/><circle cx="870" cy="276" r="4.5"/>
    <circle cx="1013" cy="318" r="4.5"/><circle cx="74" cy="503" r="4.5"/><circle cx="997" cy="524" r="4.5"/>
    <circle cx="54" cy="1017" r="4.5"/><circle cx="929" cy="1165" r="4.5"/><circle cx="125" cy="1205" r="4.5"/>
    <circle cx="215" cy="1247" r="4.5"/><circle cx="442" cy="1247" r="4.5"/><circle cx="870" cy="1231" r="4.5"/>
    <circle cx="1014" cy="1281" r="4.5"/><circle cx="1423" cy="90" r="4.5"/><circle cx="1906" cy="44" r="4.5"/>
    <circle cx="2152" cy="76" r="4.5"/><circle cx="2012" cy="143" r="4.5"/><circle cx="1462" cy="219" r="4.5"/>
    <circle cx="2160" cy="272" r="4.5"/><circle cx="1284" cy="313" r="4.5"/><circle cx="2219" cy="473" r="4.5"/>
    <circle cx="1395" cy="505" r="4.5"/><circle cx="2009" cy="536" r="4.5"/><circle cx="1300" cy="604" r="4.5"/>
    <circle cx="2244" cy="746" r="4.5"/>
  </svg>

  <section class="back-cover">
    <p class="tagline">When happily ever falls apart,<br>all you can do is move<br>forward…and reminisce.</p>
    <p class="blurb">Marisol Ahn returns home from<br>college following a tragic incident she<br>can’t bring herself to talk about and a breakup<br>with her boyfriend, Theo Marsh. Finding<br>it difficult to confront her traumas,<br>she begins therapy. Marisol takes the<br>therapist on a rollercoaster journey of her<br>college life, retelling the events that caused<br>her relationship to spiral out of control and<br>led to her dropping out of pre-med despite that<br>being her life-long dream. Marisol sets out to<br>remember how things were before everything<br>got so messed up, and figure out how to<br>continue living now that they are.</p>
    <p class="author-bio"><strong>Brenna Quill</strong> is the author of <em>The Restless and Bold</em>. She is a self published writer from Las Vegas who likes to pretend she’s currently in a New York bookstore, drinking a latte, while listening to a carefully curated playlist. When she’s not writing, Brenna is taking care of her plant babies and cuddling with the cutest puppy in the world.</p>
    <div class="barcode-area" aria-label="Barcode space"></div>
  </section>

  <section class="spine">
    <p class="spine-author">BRENNA QUILL</p>
    <p class="spine-title">The Weight of Daylight</p>
  </section>

  <section class="front-cover">
    <h1 class="front-title">
      <span class="word-small">The</span>
      <span class="word-large">Weight</span>
      <span class="word-of">of</span>
      <span class="word-large">Daylight</span>
    </h1>
    <p class="front-author">BRENNA QUILL</p>
    <div class="cover-illustration" role="img" aria-label="Illustration of a young woman with long brown hair in a red top looking over her shoulder, surrounded by blue silhouettes of a crowd"></div>
  </section>
</main>
</body>
</html>
```